Luxury château wedding venue needs magazine advertisement targeting gay market

We need a full-page, full-colour glossy magazine advertisement targeting the gay market. We need to communicate that there is a luxury château in France which is gay-friendly and available to be used as a destination wedding venue with 5* accommodation. The property can be hired exclusively or suite-by-suite. The château is moated with a chapel and banqueting halls seating between 18 and 150. 20m heated pool for guests, large forest. Wedding planner and co-ordinator available.

Target Market(s)

25-45 gay men and women AB international but principally English and French speaking

Industry/Entity Type

Wedding

Requirements
Must have
• Trim 210 x 285 / Bleed 216 x 291 / Type 183 x 255. Wedding or Civil Partnership references. Subtle, understated and quality gay image. Loire Valley France. www.chateaudemorvillac.com (F) 00 33 (0)2 47 83 19 25 0r UK 00 44 (0)7582 649307 Nearest airports: Tours, Nantes, Poitiers, Paris
Nice to have
• Venue also available for private holidays and exclusive parties

```html
<!DOCTYPE html>
<html lang="en">
<head>
<meta charset="utf-8">
<title>Château de Morvillac – Luxury Destination Wedding Venue</title>
<link rel="stylesheet" href="https://fonts.googleapis.com/css2?family=Cinzel:wght@500&family=Lobster+Two:ital,wght@1,700&family=Lato:ital,wght@0,400;0,700;0,900;1,400&display=swap">
<style>
:root{
  --crimson:#c41f3b;
  --crimson-dark:#9e1830;
  --paper:#e9e9eb;
  --ink:#3a3a3e;
  --ink-soft:#5a5a60;
  --white:#ffffff;
}
*{margin:0;padding:0;box-sizing:border-box}
html,body{width:891px;height:1200px;overflow:hidden;background:var(--paper)}
.advert{position:relative;width:891px;height:1200px;background:var(--paper);font-family:'Lato',sans-serif;color:var(--ink);overflow:hidden}

.hero-photo{position:absolute;left:0;top:0;width:891px;height:590px;
  background:linear-gradient(110deg,#f6f1ef 0%,#efe3e2 30%,#e7c9cd 48%,#f3ece9 62%,#ddd6d8 100%)}
.hero-veil{position:absolute;left:0;top:0;width:891px;height:590px;
  background:linear-gradient(90deg,rgba(255,255,255,.55) 0%,rgba(255,255,255,.15) 50%,rgba(255,255,255,.45) 100%)}

.brand{position:absolute;top:92px;left:0;width:891px;display:flex;justify-content:center;align-items:center;gap:14px}
.brand-mark{width:14px;height:14px;background:var(--ink)}
.brand-name{font-family:'Cinzel',serif;font-weight:500;font-size:32px;letter-spacing:4px;color:var(--ink)}

.headline{position:absolute;left:48px;top:318px;font-family:'Lobster Two',cursive;font-style:italic;font-weight:700;font-size:44px;line-height:46px;color:var(--crimson)}
.venue-line{position:absolute;left:48px;top:420px;font-size:24px;color:var(--crimson)}
.stars{position:absolute;left:48px;top:452px;font-size:34px;font-weight:900;color:var(--crimson);letter-spacing:.5px}
.region{position:absolute;left:48px;top:498px;font-size:22px;color:var(--ink)}

.intro{position:absolute;left:478px;top:180px;width:380px;font-style:italic;font-size:18.5px;line-height:25px;color:var(--ink);text-align:right}

.gallery{position:absolute;top:600px;left:24px;display:flex;gap:14px}
.gallery-photo{height:218px}
.photo-interior{width:310px;background:linear-gradient(135deg,#6b4a33,#b99870 55%,#5a3d2b)}
.photo-table{width:226px;background:linear-gradient(160deg,#e8e3dc,#f7f4ef 50%,#c84a5a)}
.photo-aerial{width:283px;background:linear-gradient(180deg,#a9b7c6 0%,#c9c6bd 35%,#7f9a5e 70%,#5f7d44)}

.band-wedding{position:absolute;left:0;top:858px;width:640px;height:48px;background:var(--crimson);padding-left:48px;
  font-family:'Lobster Two',cursive;font-style:italic;font-weight:700;font-size:32px;line-height:48px;color:var(--white)}
.details{position:absolute;left:30px;top:916px;width:832px;font-size:13.5px;line-height:19px;color:var(--ink-soft)}
.band-extra{position:absolute;left:0;top:972px;width:891px;height:40px;background:var(--crimson);padding-left:30px;
  font-family:'Lobster Two',cursive;font-style:italic;font-weight:700;font-size:25px;line-height:40px;color:var(--white)}

.contact{position:absolute;left:0;top:1046px;width:891px;text-align:center;font-size:16px;line-height:24px;color:var(--ink)}

.bouquet{position:absolute;left:722px;top:1010px;width:190px;height:190px;border-radius:50%;
  background:radial-gradient(circle at 45% 45%,#e0455f 0%,#b5172f 55%,#7a0f22 100%)}
</style>
</head>
<body>
<main class="advert">
  <div class="hero-photo" role="img" aria-label="Bride holding a bouquet of pale pink and white roses"></div>
  <div class="hero-veil"></div>

  <header class="brand">
    <span class="brand-mark"></span>
    <span class="brand-name">Château de Morvillac</span>
  </header>

  <h1 class="headline">Step inside and<br>experience the Luxury</h1>
  <p class="venue-line">Luxury Destination Venue with</p>
  <p class="stars">5+ ACCOMMODATION</p>
  <p class="region">in The Loire Valley, France</p>

  <p class="intro">High ceilings tower over Stone floors juxtaposed with warm wooden parquetry. The sweet smokey smell of a log fire mingling with the scent of freshly-picked flowers. Music floats gently from the nearby chapel, accompanying the gentle pop of a cork as your host pours a chilled glass of sparkling wine. Everything confirms that you have indeed discovered the perfect venue.</p>

  <section class="gallery">
    <div class="gallery-photo photo-interior" role="img" aria-label="Grand château hallway with staircase and antique furniture"></div>
    <div class="gallery-photo photo-table" role="img" aria-label="Wedding table setting with white plates and red flowers"></div>
    <div class="gallery-photo photo-aerial" role="img" aria-label="Aerial view of the moated château among fields and forest"></div>
  </section>

  <div class="band-wedding">Your wedding · Your way</div>
  <p class="details">The property can be hired exclusively or suite-by-suite. The château is moated with a chapel and banqueting halls seating between 18 and 150. 20m heated pool for guests, large forest. Wedding planner and co-ordinator available.</p>
  <div class="band-extra">Venue also available for private holidays and exclusive parties</div>

  <address class="contact" style="font-style:normal">
    Château de Morvillac, 37130 Langeville<br>
    Web : www.chateaudemorvillac.com<br>
    Email : contact@chateaudemorvillac.com<br>
    Telephone: +33 (0)2 47 83 19 25 (FR) +44 (0)7582 649307 (UK)
  </address>

  <div class="bouquet" role="img" aria-label="Bouquet of deep red roses"></div>
</main>
</body>
</html>
```